Medical Device - Case Study Template

We need a TEMPLATE that we can reuse to write various case studies about the medical equipment solutions we provide. It will be a double sided letter sized with a modern design that conveys a feeling of expertise, innovation and highly personable service AND be consistent with the brand guide. The content will be divided into a few sections:

- Situation (200-250 words)
- Challenge (100-120 words)
- Solution (100-120 words)
- Results (100-120 words)
- Conclusion (100-120 words)

Additionally, there will need to be a call to action, inviting people to send an email for more information and a short "About Valtu" section (approx. 40 words).

For device picture placeholders, feel free to use any random small benchtop medical device.

```html
<!DOCTYPE html>
<html lang="en">
<head>
<meta charset="utf-8">
<title>Valtu Medical Technology – Case Study Template</title>
<link rel="stylesheet" href="https://fonts.googleapis.com/css2?family=Montserrat:wght@400;600;700;800&family=Open+Sans:wght@400;600&display=swap">
<style>
  :root{
    --orange:#f5822f;
    --blue:#78a3bf;
    --blue-deep:#5f8fae;
    --ink:#2b2b2b;
    --white:#ffffff;
    --stage:#e6e7e9;
    --photo-a:#cfe3ef;
    --photo-b:#8fb4cc;
    --photo-c:#eef1f3;
    --photo-d:#c8cdd1;
  }
  *{box-sizing:border-box;margin:0;padding:0}
  html,body{width:1200px;height:792px;overflow:hidden;background:var(--stage)}
  body{position:relative;font-family:"Open Sans",Arial,sans-serif;color:var(--ink)}
  .page{position:absolute;top:72px;width:512px;height:661px;background:var(--white);overflow:hidden;box-shadow:0 6px 18px rgba(0,0,0,.18)}
  .page--front{left:68px}
  .page--back{left:621px}
  .backdrop{position:absolute;inset:0;width:512px;height:661px}
  .abs{position:absolute}

  /* front */
  .brand{left:33px;top:34px;display:flex;align-items:center;gap:8px}
  .brand__dot{width:20px;height:20px;border-radius:50%;background:var(--orange)}
  .brand__name{font-family:"Montserrat",sans-serif;font-weight:600;font-size:34px;line-height:1;color:var(--blue-deep);letter-spacing:1px}
  .brand__tag{left:62px;top:76px;font-family:"Montserrat",sans-serif;font-size:11.5px;color:var(--blue-deep);letter-spacing:.6px}
  .hero-photo{left:259px;top:0;width:253px;height:318px}
  .headline{left:41px;top:168px;color:var(--white);font-family:"Montserrat",sans-serif;font-size:23px;line-height:26px}
  .headline b{font-weight:800;display:block}
  .subhead{left:41px;top:227px;color:var(--white);font-family:"Montserrat",sans-serif;font-size:13.5px}
  .about-title{left:41px;top:255px;width:261px;padding-bottom:4px;border-bottom:1.5px solid var(--white);color:var(--white);font-family:"Montserrat",sans-serif;font-size:21px;font-weight:400}
  .about-title b{font-weight:800}
  .about-text{left:41px;top:290px;width:264px;color:var(--white);font-size:7.1px;line-height:9.7px}

  .hex-frame{position:absolute;width:128px;height:142px;clip-path:polygon(50% 0,100% 25%,100% 75%,50% 100%,0 75%,0 25%);background:#dfe9f0;padding:4px}
  .hex-photo{width:100%;height:100%;clip-path:polygon(50% 0,100% 25%,100% 75%,50% 100%,0 75%,0 25%)}
  .photo--room{background:linear-gradient(160deg,var(--photo-c),var(--photo-d))}
  .photo--theatre{background:linear-gradient(160deg,var(--photo-a),var(--photo-b))}
  .photo--lab{background:linear-gradient(160deg,#7fd0e0,#3d7ea6)}

  .product{position:absolute;top:508px;width:117px;text-align:center}
  .product__name{font-family:"Montserrat",sans-serif;font-weight:700;font-size:11.5px;color:var(--orange);line-height:15px;white-space:nowrap}
  .product__model{font-family:"Montserrat",sans-serif;font-size:11.5px;color:var(--blue-deep);line-height:15px;padding-bottom:3px;border-bottom:1px solid var(--orange)}
  .product__text{font-size:6.6px;line-height:9.1px;margin-top:7px;color:var(--ink)}
  .page--back .product__name,.page--back .product__model{color:var(--white)}
  .page--back .product__model{border-bottom-color:var(--white)}
  .page--back .product__text{color:#fde3cf}

  .contact-bar{position:absolute;left:0;bottom:0;width:512px;height:41px;display:flex;align-items:center;justify-content:center;gap:14px;color:var(--white);font-family:"Montserrat",sans-serif;font-weight:700;font-size:16.5px}
  .contact-bar--orange{background:var(--orange)}
  .contact-bar--blue{background:var(--blue);border-top:3px solid var(--white);height:44px}
  .contact-bar__item{display:flex;align-items:center;gap:5px}
  .contact-bar__sep{width:1.5px;height:18px;background:var(--white)}

  /* back */
  .section-title{position:absolute;height:28px;border:1.3px solid var(--orange);color:var(--orange);font-family:"Montserrat",sans-serif;font-weight:800;font-size:20px;line-height:26px;padding-left:15px;letter-spacing:.5px}
  .section-text{position:absolute;font-size:7.1px;line-height:9.7px;color:var(--ink)}
  .col-left{left:41px;width:172px}
  .col-right{left:271px;width:200px}
  .divider{left:241px;top:37px;width:1.3px;height:313px;background:var(--blue)}
</style>
</head>
<body>

<!-- FRONT -->
<section class="page page--front">
  <svg class="backdrop" viewBox="0 0 512 661" aria-hidden="true">
    <polygon points="0,115 106,134 0,152" fill="var(--orange)"/>
    <polygon points="0,152 265,105 512,105 512,387 319,420 188,447 0,480" fill="var(--blue)"/>
    <polygon points="319,420 512,387 512,494 341,473" fill="var(--orange)"/>
  </svg>

  <div class="abs brand"><span class="brand__dot"></span><span class="brand__name">valtu</span></div>
  <div class="abs brand__tag">Medical Technology</div>

  <svg class="abs hero-photo" viewBox="0 0 253 318" role="img" aria-label="Photo of a bright treatment room with a white examination chair and benchtop device">
    <defs><linearGradient id="heroGrad" x1="0" y1="0" x2="1" y2="1"><stop offset="0" stop-color="#f3f4f5"/><stop offset="1" stop-color="#c9ced2"/></linearGradient></defs>
    <polygon points="6,59 104,0 253,0 253,266 153,318 0,230" fill="#dbe7ef"/>
    <polygon points="12,62 106,6 253,6 253,262 153,311 6,226" fill="url(#heroGrad)"/>
  </svg>

  <h1 class="abs headline">YOUR BRAND<b>HEADING HERE</b></h1>
  <p class="abs subhead">Subheading place here</p>
  <h2 class="abs about-title">ABOUT <b>VALTU</b></h2>
  <p class="abs about-text">Lorem ipsum dolor sit amet, consectetur adipiscing elit, sed do eiusmod tempor incididunt ut labore et dolore magna aliqua. Ut enim ad minim veniam, quis nostrud exercitation ullamco laboris nisi ut aliquip ex ea commodo consequat.<br>Duis aute irure dolor in reprehenderit in voluptate velit esse cillum dolore eu fugiat nulla pariatur.</p>

  <div class="hex-frame" style="left:34px;top:357px"><div class="hex-photo photo--room" role="img" aria-label="Photo of a benchtop examination microscope and monitor"></div></div>
  <div class="hex-frame" style="left:191px;top:357px"><div class="hex-photo photo--theatre" role="img" aria-label="Photo of an operating theatre with surgical lamps"></div></div>
  <div class="hex-frame" style="left:349px;top:357px"><div class="hex-photo photo--lab" role="img" aria-label="Photo of a laboratory workstation with microscope and screen"></div></div>

  <div class="product" style="left:40px"><div class="product__name">Your Product Name</div><div class="product__model">Model No</div><p class="product__text">Lorem ipsum dolor sit amet, consectetur adipiscing elit, sed do eiusmod tempor incididunt ut labore et dolore magna aliqua. Ut enim ad minim veniam, quis nostrud exercitation ullamco laboris nisi ut aliquip ex ea commodo consequat.</p></div>
  <div class="product" style="left:197px"><div class="product__name">Your Product Name</div><div class="product__model">Model No</div><p class="product__text">Lorem ipsum dolor sit amet, consectetur adipiscing elit, sed do eiusmod tempor incididunt ut labore et dolore magna aliqua. Ut enim ad minim veniam, quis nostrud exercitation ullamco laboris nisi ut aliquip ex ea commodo consequat.</p></div>
  <div class="product" style="left:355px"><div class="product__name">Your Product Name</div><div class="product__model">Model No</div><p class="product__text">Lorem ipsum dolor sit amet, consectetur adipiscing elit, sed do eiusmod tempor incididunt ut labore et dolore magna aliqua. Ut enim ad minim veniam, quis nostrud exercitation ullamco laboris nisi ut aliquip ex ea commodo consequat.</p></div>

  <footer class="contact-bar contact-bar--orange">
    <span class="contact-bar__item"><svg width="14" height="14" viewBox="0 0 14 14" aria-hidden="true"><circle cx="7" cy="7" r="6" fill="none" stroke="#fff" stroke-width="1.2"/><path d="M5 4l1 1.6-.7.8c.4.9 1 1.5 1.9 1.9l.8-.7L9.6 8.6 9 10c-2.6-.3-4.7-2.4-5-5z" fill="#fff"/></svg>0100-555-0178</span>
    <span class="contact-bar__sep"></span>
    <span class="contact-bar__item"><svg width="15" height="11" viewBox="0 0 15 11" aria-hidden="true"><rect x=".6" y=".6" width="13.8" height="9.8" fill="none" stroke="#fff" stroke-width="1.2"/><path d="M.6.6l6.9 5.5L14.4.6" fill="none" stroke="#fff" stroke-width="1.2"/></svg>info@valtumedicaltech.com</span>
  </footer>
</section>

<!-- BACK -->
<section class="page page--back">
  <svg class="backdrop" viewBox="0 0 512 661" aria-hidden="true">
    <polygon points="0,372 330,420 0,474" fill="var(--blue)"/>
    <polygon points="0,474 512,387 512,661 0,661" fill="var(--orange)"/>
  </svg>

  <h2 class="section-title col-left" style="top:37px">SITUATION</h2>
  <p class="section-text col-left" style="top:74px">Lorem ipsum dolor sit amet, consectetur adipiscing elit, sed do eiusmod tempor incididunt ut labore et dolore magna aliqua. Ut enim ad minim veniam, quis nostrud exercitation ullamco laboris nisi ut aliquip ex ea commodo consequat. Duis aute irure dolor in reprehenderit in voluptate velit esse cillum dolore eu fugiat nulla pariatur. Excepteur sint occaecat cupidatat non proident, sunt in culpa qui officia deserunt mollit anim id est laborum.<br>Sed ut perspiciatis unde omnis iste natus error sit voluptatem accusantium doloremque laudantium, totam rem aperiam, eaque ipsa quae ab illo inventore veritatis et quasi architecto beatae vitae dicta sunt explicabo.</p>

  <h2 class="section-title col-left" style="top:224px">CHALLENGE</h2>
  <p class="section-text col-left" style="top:262px">Lorem ipsum dolor sit amet, consectetur adipiscing elit, sed do eiusmod tempor incididunt ut labore et dolore magna aliqua. Ut enim ad minim veniam, quis nostrud exercitation ullamco laboris nisi ut aliquip ex ea commodo consequat. Duis aute irure dolor in reprehenderit in voluptate velit esse cillum dolore eu fugiat nulla pariatur. Excepteur sint occaecat cupidatat non proident, sunt in culpa qui officia deserunt mollit anim id est laborum.</p>

  <div class="abs divider"></div>

  <h2 class="section-title col-right" style="top:37px">SOLUTION</h2>
  <p class="section-text col-right" style="top:74px">Lorem ipsum dolor sit amet, consectetur adipiscing elit, sed do eiusmod tempor incididunt ut labore et dolore magna aliqua. Ut enim ad minim veniam, quis nostrud exercitation ullamco laboris nisi ut aliquip ex ea commodo consequat. Duis aute irure dolor in reprehenderit in voluptate velit esse cillum dolore eu fugiat nulla pariatur.</p>

  <h2 class="section-title col-right" style="top:146px">RESULTS</h2>
  <p class="section-text col-right" style="top:182px">Lorem ipsum dolor sit amet, consectetur adipiscing elit, sed do eiusmod tempor incididunt ut labore et dolore magna aliqua. Ut enim ad minim veniam, quis nostrud exercitation ullamco laboris nisi ut aliquip ex ea commodo consequat. Duis aute irure dolor in reprehenderit in voluptate velit esse cillum dolore eu fugiat nulla pariatur.</p>

  <h2 class="section-title col-right" style="top:254px">CONCLUSION</h2>
  <p class="section-text col-right" style="top:290px">Lorem ipsum dolor sit amet, consectetur adipiscing elit, sed do eiusmod tempor incididunt ut labore et dolore magna aliqua. Ut enim ad minim veniam, quis nostrud exercitation ullamco laboris nisi ut aliquip ex ea commodo consequat. Duis aute irure dolor in reprehenderit in voluptate velit esse cillum dolore eu fugiat nulla pariatur.</p>

  <div class="hex-frame" style="left:37px;top:357px"><div class="hex-photo photo--room" role="img" aria-label="Photo of a benchtop examination microscope and monitor"></div></div>
  <div class="hex-frame" style="left:194px;top:357px"><div class="hex-photo photo--theatre" role="img" aria-label="Photo of an operating theatre with surgical lamps"></div></div>
  <div class="hex-frame" style="left:352px;top:357px"><div class="hex-photo photo--lab" role="img" aria-label="Photo of a laboratory workstation with microscope and screen"></div></div>

  <div class="product" style="left:41px"><div class="product__name">Your Product Name</div><div class="product__model">Model No</div><p class="product__text">Lorem ipsum dolor sit amet, consectetur adipiscing elit, sed do eiusmod tempor incididunt ut labore et dolore magna aliqua. Ut enim ad minim veniam, quis nostrud exercitation ullamco laboris nisi ut aliquip ex ea commodo consequat.</p></div>
  <div class="product" style="left:199px"><div class="product__name">Your Product Name</div><div class="product__model">Model No</div><p class="product__text">Lorem ipsum dolor sit amet, consectetur adipiscing elit, sed do eiusmod tempor incididunt ut labore et dolore magna aliqua. Ut enim ad minim veniam, quis nostrud exercitation ullamco laboris nisi ut aliquip ex ea commodo consequat.</p></div>
  <div class="product" style="left:356px"><div class="product__name">Your Product Name</div><div class="product__model">Model No</div><p class="product__text">Lorem ipsum dolor sit amet, consectetur adipiscing elit, sed do eiusmod tempor incididunt ut labore et dolore magna aliqua. Ut enim ad minim veniam, quis nostrud exercitation ullamco laboris nisi ut aliquip ex ea commodo consequat.</p></div>

  <footer class="contact-bar contact-bar--blue">
    <span class="contact-bar__item"><svg width="14" height="14" viewBox="0 0 14 14" aria-hidden="true"><circle cx="7" cy="7" r="6" fill="none" stroke="#fff" stroke-width="1.2"/><path d="M5 4l1 1.6-.7.8c.4.9 1 1.5 1.9 1.9l.8-.7L9.6 8.6 9 10c-2.6-.3-4.7-2.4-5-5z" fill="#fff"/></svg>0100-555-0178</span>
    <span class="contact-bar__sep"></span>
    <span class="contact-bar__item"><svg width="15" height="11" viewBox="0 0 15 11" aria-hidden="true"><rect x=".6" y=".6" width="13.8" height="9.8" fill="none" stroke="#fff" stroke-width="1.2"/><path d="M.6.6l6.9 5.5L14.4.6" fill="none" stroke="#fff" stroke-width="1.2"/></svg>info@valtumedicaltech.com</span>
  </footer>
</section>

</body>
</html>
```